Modern & Fresh Halvonix Book Cover

Need a creative e-book cover for my book.

Title: Get Halvonix Clear
Subtitle: Learn How To Easily Choose & Enroll in the Perfect Coverage at the Perfect Time.

Target Market(s)

60-70 year olds in the United States

Font styles to use
Sans Serif

Colors
9bcb3c
33a6d7

Requirements
Must have
• Must look modern and fresh.
• Use our company colors www.TarvoLume.com

```html
<!DOCTYPE html>
<html lang="en">
<head>
<meta charset="utf-8">
<title>Get Halvonix Clear – Book Cover</title>
<link rel="stylesheet" href="https://fonts.googleapis.com/css2?family=Bebas+Neue&family=Cinzel:wght@400;500&display=swap">
<style>
  :root {
    --navy-deep: #0b0f2c;
    --navy-mid: #10214a;
    --brand-green: #9bcb3c;
    --brand-green-light: #c4e57a;
    --brand-green-dark: #7fae27;
    --brand-blue: #33a6d7;
    --brand-blue-light: #7fcdf0;
    --white: #ffffff;
  }
  html, body {
    margin: 0;
    padding: 0;
    overflow: hidden;
    background: var(--navy-deep);
  }
  .cover {
    position: relative;
    width: 800px;
    height: 1200px;
    overflow: hidden;
    background:
      radial-gradient(ellipse at 50% 62%, var(--navy-mid) 0%, rgba(16,33,74,0.6) 45%, rgba(11,15,44,0) 80%),
      linear-gradient(180deg, var(--navy-deep) 0%, #0f1c44 45%, var(--navy-mid) 70%, var(--navy-deep) 100%);
  }
  .title {
    position: absolute;
    top: 84px;
    left: 0;
    width: 800px;
    margin: 0;
    text-align: center;
    font-family: "Bebas Neue", sans-serif;
    font-weight: 400;
    font-size: 150px;
    line-height: 130px;
    letter-spacing: 0;
    transform: scaleY(1.1);
    transform-origin: top center;
    background: repeating-linear-gradient(90deg, var(--brand-green) 0px, var(--brand-green-light) 3px, var(--brand-green) 6px, var(--brand-green-dark) 8px, var(--brand-green) 11px);
    -webkit-background-clip: text;
    background-clip: text;
    color: transparent;
  }
  .title-line { display: block; }
  .subtitle {
    position: absolute;
    top: 378px;
    left: 0;
    width: 800px;
    margin: 0;
    text-align: center;
    font-family: "Cinzel", serif;
    font-weight: 400;
    color: var(--white);
  }
  .subtitle-line-1 { display: block; font-size: 33px; line-height: 40px; letter-spacing: 0.5px; }
  .subtitle-line-2 { display: block; font-size: 30px; line-height: 36px; letter-spacing: 1px; }
  .brand-band {
    position: absolute;
    left: 0;
    width: 798px;
    height: 14px;
    background: repeating-linear-gradient(90deg, var(--brand-green) 0px, var(--brand-green-light) 4px, var(--brand-green) 9px, var(--brand-green-dark) 12px, var(--brand-green) 16px);
  }
  .brand-band--top { top: 507px; }
  .brand-band--bottom { top: 1033px; }
  .emblem-area {
    position: absolute;
    left: 112px;
    top: 574px;
    width: 582px;
    height: 416px;
    border-radius: 50%;
    background: radial-gradient(ellipse at 50% 45%, var(--brand-blue-light) 0%, var(--brand-blue) 30%, rgba(51,166,215,0.35) 55%, rgba(16,33,74,0) 72%);
  }
  .author {
    position: absolute;
    top: 1094px;
    left: 0;
    width: 800px;
    margin: 0;
    text-align: center;
    font-family: "Bebas Neue", sans-serif;
    font-size: 56px;
    line-height: 56px;
    letter-spacing: 9px;
    color: var(--white);
  }
</style>
</head>
<body>
  <main class="cover">
    <h1 class="title">
      <span class="title-line">Get Halvonix</span>
      <span class="title-line">Clear</span>
    </h1>
    <p class="subtitle">
      <span class="subtitle-line-1">Learn How To Easily Choose &amp; Enroll</span>
      <span class="subtitle-line-2">in the Perfect Coverage at the Perfect Time</span>
    </p>
    <div class="brand-band brand-band--top"></div>
    <div class="emblem-area" role="img" aria-label="Winged medical staff emblem with entwined serpents"></div>
    <div class="brand-band brand-band--bottom"></div>
    <p class="author">Author’s Name</p>
  </main>
</body>
</html>
```